Web design for sitter site

We will be launching a sitter site in the coming months that focuses on sitters for children. The name of this site will be KinWatch.com
We will need:
1. main page design
2. site logo designed
3. subpages as well for the look of people's profiles, and job listings, etc (see links below)
We only need the design, photos, font files, etc. We do not need this site coded (no html), a ps job is fine.
Some competing sites in the space include - tendhaven.com and mindly.com
http://www.example-guardia.com/images/profile1.jpg
http://brookvaleshelf.example/wp-content/uploads/2013/09/mindly-review.png
http://www.pinecrestuni.example/hr/photos/tend_haven2.jpg
Thanks for your interest!
Target Market(s)
Mothers of children, mainly women
Industry/Entity Type
Online
Look and feel

```html
<!DOCTYPE html>
<html lang="en">
<head>
<meta charset="utf-8">
<title>KinWatch – Home</title>
<link rel="stylesheet" href="https://fonts.googleapis.com/css2?family=Arimo:wght@400;700&family=Indie+Flower&display=swap">
<style>
:root{
  --sky:#1fa8ee;
  --sky-deep:#0f8fd6;
  --sky-pale:#e6f5fd;
  --leaf:#35c27a;
  --leaf-deep:#2aa866;
  --ink:#1f5f8f;
  --text:#333;
  --muted:#8a8a8a;
  --white:#fff;
  --rule:#d9e6ef;
  --grey-btn:#9a9a9a;
}
*{box-sizing:border-box;margin:0;padding:0}
html,body{width:713px;height:1200px;overflow:hidden;background:var(--white)}
body{position:relative;font-family:"Arimo",Arial,sans-serif;color:var(--text)}
.hand{font-family:"Indie Flower",cursive}
.abs{position:absolute}

/* hero */
.hero-photo{position:absolute;left:0;top:80px;width:713px;height:440px;
  background:linear-gradient(100deg,#b89a86 0%,#d9c6b4 30%,#9fb4c2 55%,#6f7b6c 80%,#c8b7a3 100%)}
.header-band{position:absolute;left:0;top:0;width:713px;height:130px}
.band-bottom{position:absolute;left:0;top:520px;width:713px;height:17px;background:var(--sky)}
.brand{left:28px;top:34px;color:var(--white);font-family:"Arimo",Arial,sans-serif;font-weight:700;font-size:34px;line-height:1}
.nav{left:263px;top:0;display:flex}
.nav a{display:block;height:47px;line-height:52px;padding:0 10px;color:var(--white);font-size:12px;text-decoration:none;margin-right:4px}
.nav a.active{background:var(--leaf-deep)}
.search{left:585px;top:25px;width:99px;height:20px;background:var(--white);font-size:9px;color:var(--muted);padding:4px 6px}
.adv-search{left:631px;top:52px;color:var(--white);font-size:7px}
.hero-line{left:76px;top:232px;color:var(--white);font-size:34px;line-height:40px}

/* sign up */
.signup{left:476px;top:120px;width:208px;height:263px;background:rgba(31,168,238,.95);color:var(--white);padding:12px 10px}
.signup h2{font-size:14px;font-weight:700}
.signup .signin{position:absolute;right:10px;top:16px;font-size:9px;opacity:.7}
.signup p{font-size:9px;line-height:12px;margin:10px 0 8px}
.field{height:20px;border:1px solid rgba(255,255,255,.8);margin-bottom:8px;font-size:9px;line-height:18px;padding-left:8px;color:rgba(255,255,255,.85)}
.row{display:flex;gap:6px}
.row .field{flex:1}
.check{display:flex;align-items:center;gap:8px;font-size:8px;margin-bottom:8px;flex:1}
.box{width:20px;height:20px;border:1px solid var(--white);flex:none}
.signup .terms{font-size:8px;line-height:10px}
.signup .terms span{color:#ffe9a8}
.signup .go{position:absolute;left:0;bottom:0;width:208px;height:30px;background:var(--leaf);text-align:center;line-height:30px;font-size:11px;font-weight:700}

/* how it works */
.how{left:40px;top:558px;color:var(--sky-deep);font-size:28px;display:flex;align-items:center;gap:14px}
.how .sel{width:179px;height:28px;border:1px solid var(--sky);font-size:15px;color:var(--text);display:flex;align-items:center;justify-content:center;gap:12px}
.step{width:121px;height:57px;border-radius:5px;color:var(--white);font-size:20px;line-height:21px;display:flex;align-items:center;justify-content:center;text-align:center}
.step.green{background:var(--leaf)}
.step.blue{background:var(--sky)}
.arrow{width:12px;height:10px}
.rule{left:36px;width:620px;height:1px;background:var(--rule)}

/* quick */
.quick{left:32px;top:832px;color:var(--sky-deep);font-size:29px}
.label{font-size:16px;color:var(--sky-deep)}
.dropdown{height:26px;border:1px solid var(--sky);font-size:11px;padding:0 8px;display:flex;align-items:center;justify-content:space-between}
.list{background:var(--sky);color:var(--white);font-size:11px}
.list li{list-style:none;height:25px;line-height:25px;padding-left:8px}
.list li.on{background:var(--sky-deep)}
.card{left:280px;top:903px;width:187px;height:117px;background:var(--sky-pale);border:1px solid #b9d6e8;box-shadow:0 2px 5px rgba(0,0,0,.2);padding:8px 10px;font-size:9px}
.card .avatar{width:23px;height:23px;background:linear-gradient(#c67b4a,#e4b48c);border:1px solid #999}
.card .name{font-size:11px;color:#444}
.card .meta{font-size:8px;color:#666}
.card .quote{margin-top:10px;color:#555;font-style:italic;line-height:11px}
.card .skills{margin-top:8px;font-weight:700;color:#555}
.sitter{display:flex;align-items:center;gap:8px;font-size:9px;color:var(--ink);height:22px}
.tick{width:17px;height:17px;border:1px solid #aaa;background:var(--white)}
.btn{color:var(--white);font-size:10px;display:flex;align-items:center;justify-content:center}

/* footer */
.copy{left:34px;top:1122px;font-size:9px;color:var(--ink)}
.social{left:32px;top:1142px;display:flex;gap:4px}
.social span{width:24px;height:24px;display:block}
.links{left:506px;top:1158px;font-size:9px;color:var(--ink)}
.foot-band{left:0;top:1183px;width:713px;height:17px;background:var(--sky)}
</style>
</head>
<body>

<div class="hero-photo" role="img" aria-label="Photo of a mother and her small son playing with toy cars on the floor"></div>

<svg class="header-band" viewBox="0 0 713 130" preserveAspectRatio="none" aria-hidden="true">
  <path d="M0 0H713V112C600 128 520 100 420 112C320 126 200 96 100 114C60 120 25 118 0 112Z" fill="#1fa8ee"/>
</svg>

<div class="abs brand">KinWatch</div>

<nav class="abs nav hand">
  <a class="active" href="#">Home Care</a>
  <a href="#">Child Care</a>
  <a href="#">Pet Care</a>
  <a href="#">Senior Care</a>
</nav>
<div class="abs search">search</div>
<div class="abs adv-search">Advance Search</div>

<div class="abs hero-line hand">Never worry, we're<br>here to help ...</div>

<form class="abs signup">
  <h2>Free Sign Up!</h2>
  <span class="signin">Sign In</span>
  <p>Sign up now and start searching a sitter for your baby, pet, or even to your elderly love ones!</p>
  <div class="field">email address</div>
  <div class="row"><div class="field">Password</div><div class="field">Confirm Password</div></div>
  <div class="row">
    <div class="check"><span class="box"></span>I'm a parent</div>
    <div class="check"><span class="box"></span>I'm a caregiver</div>
  </div>
  <div class="field">ZIP Code or City, State</div>
  <div class="check terms"><span class="box"></span><div>I agree to the <span>Terms of Use</span> &amp;<br><span>Privacy Policy</span> of this website</div></div>
  <div class="go">CONTINUE</div>
</form>

<div class="band-bottom"></div>

<section>
  <div class="abs how hand">How it works for a
    <div class="sel">Care giver
      <svg width="9" height="6" viewBox="0 0 9 6"><path d="M0 0H9L4.5 6Z" fill="#333"/></svg>
    </div>
    <span>?</span>
  </div>

  <div class="abs step green hand" style="left:35px;top:615px">Sign Up</div>
  <div class="abs step green hand" style="left:201px;top:615px">Create a<br>Job</div>
  <div class="abs step green hand" style="left:368px;top:615px">Hire<br>Someone</div>
  <div class="abs step green hand" style="left:535px;top:615px">Pay</div>

  <div class="abs step blue hand" style="left:35px;top:699px">Sign Up</div>
  <div class="abs step blue hand" style="left:201px;top:699px">Create a<br>Profile</div>
  <div class="abs step blue hand" style="left:368px;top:699px">Search &amp;<br>Get Hired</div>
  <div class="abs step blue hand" style="left:535px;top:699px">Get Paid</div>

  <svg class="abs arrow" style="left:172px;top:639px" viewBox="0 0 12 10"><path d="M0 3H6V0L12 5 6 10V7H0Z" fill="#c9c9c9"/></svg>
  <svg class="abs arrow" style="left:339px;top:639px" viewBox="0 0 12 10"><path d="M0 3H6V0L12 5 6 10V7H0Z" fill="#c9c9c9"/></svg>
  <svg class="abs arrow" style="left:506px;top:639px" viewBox="0 0 12 10"><path d="M0 3H6V0L12 5 6 10V7H0Z" fill="#c9c9c9"/></svg>
  <svg class="abs arrow" style="left:172px;top:723px" viewBox="0 0 12 10"><path d="M0 3H6V0L12 5 6 10V7H0Z" fill="#c9c9c9"/></svg>
  <svg class="abs arrow" style="left:339px;top:723px" viewBox="0 0 12 10"><path d="M0 3H6V0L12 5 6 10V7H0Z" fill="#c9c9c9"/></svg>
  <svg class="abs arrow" style="left:506px;top:723px" viewBox="0 0 12 10"><path d="M0 3H6V0L12 5 6 10V7H0Z" fill="#c9c9c9"/></svg>
</section>

<div class="abs rule" style="top:801px"></div>

<section>
  <div class="abs quick hand">Let's get this quick.</div>

  <div class="abs label hand" style="left:32px;top:874px">I'm looking for:</div>
  <div class="abs dropdown" style="left:32px;top:899px;width:179px">Child Care
    <svg width="9" height="6" viewBox="0 0 9 6"><path d="M0 0H9L4.5 6Z" fill="#333"/></svg></div>
  <ul class="abs list" style="left:32px;top:933px;width:179px;height:114px">
    <li class="on">Child Care</li><li>Home Care</li><li>Pet Care</li><li>Adult and Senior Care</li>
  </ul>

  <div class="abs label hand" style="left:249px;top:874px">Child Care:</div>
  <div class="abs dropdown" style="left:249px;top:899px;width:180px">Babysitters</div>
  <ul class="abs list" style="left:249px;top:933px;width:180px;height:114px">
    <li>Nannies</li><li>Babysitters</li><li>Tutors</li>
  </ul>

  <div class="abs card">
    <div style="display:flex;gap:8px;align-items:center">
      <div class="avatar" role="img" aria-label="Sitter profile photo"></div>
      <div><div class="name">Dana R. Whitlow</div><div class="meta">28yrs. ,  Arizona, USA</div></div>
    </div>
    <div class="quote">" I love kids! Hire me and you'll have no worries ;) "</div>
    <div class="skills">Skills:</div>
    <div style="color:#666;margin-top:2px">Basic Cooking, Cleaning, Etc.</div>
  </div>

  <div class="abs label hand" style="left:475px;top:874px">Babysitters:</div>
  <div class="abs" style="left:477px;top:904px">
    <div class="sitter"><svg class="tick" viewBox="0 0 17 17"><path d="M3 9L7 13 14 3" stroke="#1f5f8f" stroke-width="2" fill="none"/></svg>Dana Whitlow, 28yrs,  Arizona</div>
    <div class="sitter"><span class="tick"></span>Colin Brandt, 25yrs,  New Jersey</div>
    <div class="sitter"><span class="tick"></span>Ruth Kemper, 35yrs,  Chicago</div>
  </div>
  <div class="abs btn" style="left:579px;top:983px;width:74px;height:25px;background:var(--grey-btn)">show more</div>
  <div class="abs btn" style="left:476px;top:1020px;width:177px;height:26px;background:var(--leaf)">CONTINUE</div>
</section>

<div class="abs rule" style="top:1083px"></div>

<footer>
  <div class="abs copy">(c) copyright 2014 KinWatch.com</div>
  <div class="abs social" aria-label="Social links">
    <span style="background:#3b5a9a"></span>
    <span style="background:#3aa6e0"></span>
    <span style="background:#d0473a"></span>
    <span style="background:#c4302b"></span>
  </div>
  <div class="abs links">Terms | Policy | Careers | Contact Us</div>
  <div class="abs foot-band"></div>
</footer>

</body>
</html>
```